Mobile Dental Clinic Signage

We have a company called Coastline roving dental care.

We have 5 trucks and need the outsides of the truck designed.

Colours we like used is a sea blue, dark blue, light blue basically all the blue colours as well as grey and white. We do not like too simple but something bright and professional.

We will need the following put on the truck
- Mobile Dental Centre
- Our logo
- Contact number 1300VANSMILE
- website www.crdc-van.net.au
- all social media symbols
- Somewhere on the truck have sections where is says
servicing aged care facilities, schools, corporations and aboriginal communities.

I have attached our current signage on the mobile clinic but we need this revamped. I have also attached a previous graphic designer work to give a idea although we where not that impressed with the designs

We like the swirf look but maybe in different colours. Hope all this makes sense. And if the design can cover the windows that would be great.

```html
<!DOCTYPE html>
<html lang="en">
<head>
<meta charset="utf-8">
<title>Coastline roving dental care – Trailer Side Panel</title>
<link rel="stylesheet" href="https://fonts.googleapis.com/css2?family=Archivo:wdth,wght@62..125,400..800&display=swap">
<style>
  :root {
    --navy: #2d3192;
    --sky: #29abe2;
    --white: #ffffff;
    --frame: #b9bcc0;
    --frame-dark: #8e9196;
    --charcoal: #2b2b2b;
    --icon-blue: #3a5ba0;
    --icon-sky: #7fc6e8;
  }
  html, body {
    margin: 0;
    padding: 0;
    width: 1200px;
    height: 1000px;
    overflow: hidden;
    background: var(--white);
  }
  .canvas {
    position: relative;
    width: 1200px;
    height: 1000px;
  }
  .trailer-panel {
    position: absolute;
    left: 53px;
    top: 322px;
    width: 1094px;
    height: 232px;
    box-sizing: border-box;
    border-top: 8px solid var(--frame);
    border-bottom: 8px solid var(--frame);
    background: var(--white);
    overflow: hidden;
    font-family: "Archivo", Arial, sans-serif;
  }
  .swoosh {
    position: absolute;
    left: 0;
    top: 0;
    width: 1094px;
    height: 216px;
  }
  .headline {
    position: absolute;
    left: 29px;
    top: 18px;
    margin: 0;
    color: var(--white);
    font-size: 37px;
    font-weight: 800;
    font-stretch: 125%;
    letter-spacing: 0.5px;
    line-height: 1;
  }
  .services {
    position: absolute;
    left: 29px;
    top: 66px;
    margin: 0;
    color: var(--white);
    font-size: 22.5px;
    font-weight: 400;
    font-stretch: 112%;
    line-height: 29px;
  }
  .phone {
    position: absolute;
    left: 31px;
    top: 140px;
    margin: 0;
    color: var(--white);
    font-size: 27px;
    font-weight: 800;
    font-stretch: 125%;
    line-height: 1;
  }
  .website {
    position: absolute;
    left: 29px;
    top: 172px;
    margin: 0;
    color: var(--white);
    font-size: 25px;
    font-weight: 400;
    font-stretch: 112%;
    line-height: 1;
  }
  .brand {
    position: absolute;
    left: 680px;
    top: 70px;
    display: flex;
    align-items: center;
    gap: 14px;
  }
  .brand-mark {
    width: 46px;
    height: 46px;
    background: var(--charcoal);
  }
  .brand-name {
    margin: 0;
    color: var(--charcoal);
    font-size: 24px;
    font-weight: 400;
    font-stretch: 100%;
    line-height: 1;
  }
  .social {
    position: absolute;
    right: 20px;
    top: 163px;
    display: flex;
    gap: 11px;
  }
  .social-badge {
    width: 38px;
    height: 38px;
    border-radius: 6px;
  }
  .social-badge.primary { background: var(--icon-blue); }
  .social-badge.secondary { background: var(--icon-sky); }
</style>
</head>
<body>
  <div class="canvas">
    <section class="trailer-panel">
      <svg class="swoosh" viewBox="0 0 1094 216" aria-hidden="true">
        <path fill="var(--sky)" d="M728,0 H752 C700,90 630,205 430,216 H370 C620,190 680,70 728,0 Z"/>
        <path fill="var(--navy)" d="M0,0 H730 C680,72 615,196 378,216 H0 Z"/>
      </svg>

      <h1 class="headline">MOBILE DENTAL CENTRE</h1>
      <p class="services">Servicing aged care facilities, schools,<br>corporations and aboriginal communities.</p>
      <p class="phone">1300VANSMILE</p>
      <p class="website">www.crdc-van.net.au</p>

      <div class="brand">
        <div class="brand-mark"></div>
        <p class="brand-name">Coastline roving dental care</p>
      </div>

      <div class="social">
        <div class="social-badge primary"></div>
        <div class="social-badge secondary"></div>
      </div>
    </section>
  </div>
</body>
</html>
```